Security Services Business Card

Looking for a clean modern style business card design for a residential and commercial security solutions provider. We install and service the following
security alarm, access control, video surveillance and fire alarm. Attached are the front and back of our current business cards in PSD file format.

Target Market(s)

Security alarm clients in the commercial and residential markets

Industry/Entity Type

Security Service

Contact Information for Business Card

We are open to designers suggestion and or design ideas.

Font styles to use
Serif
Sans Serif

Colors
3276b5
33a6d7
fffefd

Requirements
Must have
• Must have company logo , first and last name , phone number , web and email address, ect....

```html
<!DOCTYPE html>
<html lang="en">
<head>
<meta charset="utf-8">
<title>Vantorra Security Systems – Business Card</title>
<link href="https://fonts.googleapis.com/css2?family=Arimo:wght@400;700&display=swap" rel="stylesheet">
<style>
  :root {
    --brand-blue: #3583c8;
    --paper-white: #fffefd;
    --backdrop: #2b2b2b;
  }
  * { margin: 0; padding: 0; box-sizing: border-box; }
  html, body { width: 1200px; height: 1015px; overflow: hidden; }
  body {
    background: var(--backdrop);
    font-family: "Arimo", Arial, sans-serif;
    position: relative;
  }
  .card {
    position: absolute;
    width: 560px;
    height: 320px;
    background: var(--brand-blue);
    overflow: hidden;
    box-shadow: 0 10px 30px rgba(0,0,0,.5);
  }
  .card--back { left: 70px; top: 110px; }
  .card--front { left: 570px; top: 560px; }

  /* Back: service list */
  .services {
    position: absolute;
    left: 70px;
    top: 52px;
    list-style: none;
  }
  .service {
    display: flex;
    align-items: center;
    height: 54px;
    margin-bottom: 1px;
  }
  .service-icon {
    width: 48px; height: 48px;
    border-radius: 50%;
    background: var(--paper-white);
    display: flex; align-items: center; justify-content: center;
    flex: none;
  }
  .service-icon svg { width: 28px; height: 28px; }
  .service-label {
    margin-left: 20px;
    color: var(--paper-white);
    font-size: 15px;
    letter-spacing: .04em;
    text-transform: uppercase;
  }

  /* Front */
  .front-art { position: absolute; inset: 0; }
  .brand {
    position: absolute;
    left: 338px; top: 94px;
    width: 200px;
    text-align: center;
    color: var(--brand-blue);
    font-weight: 700;
    font-size: 30px;
    line-height: 1;
  }
  .brand-tagline {
    display: block;
    font-size: 11px;
    letter-spacing: .32em;
    margin-top: 6px;
  }
  .contact {
    position: absolute;
    left: 36px; top: 112px;
    color: var(--paper-white);
  }
  .person-name { font-size: 22px; font-weight: 700; letter-spacing: .02em; }
  .person-role { font-size: 14px; margin-top: 2px; }
  .contact-lines { list-style: none; margin-top: 20px; font-size: 14px; line-height: 1.45; }
  .contact-lines li { display: flex; align-items: center; gap: 8px; }
  .contact-lines svg { width: 14px; height: 14px; flex: none; }
  .address { font-size: 15px; line-height: 1.4; margin-top: 18px; padding-left: 22px; }
</style>
</head>
<body>

<section class="card card--back" aria-label="Business card back">
  <ul class="services">
    <li class="service">
      <span class="service-icon">
        <svg viewBox="0 0 28 28" fill="var(--brand-blue)" aria-hidden="true">
          <rect x="3" y="3" width="5" height="5"/><rect x="10" y="3" width="5" height="5"/><rect x="17" y="3" width="5" height="5"/>
          <rect x="3" y="10" width="5" height="5"/><rect x="10" y="10" width="5" height="5"/>
          <rect x="3" y="17" width="5" height="5"/>
          <rect x="13" y="13" width="11" height="12" rx="3"/>
        </svg>
      </span>
      <span class="service-label">Access Control</span>
    </li>
    <li class="service">
      <span class="service-icon">
        <svg viewBox="0 0 28 28" fill="var(--brand-blue)" aria-hidden="true">
          <path d="M8 20v-7a6 6 0 0 1 12 0v7z"/><rect x="5" y="21" width="18" height="4" rx="1"/>
          <path d="M14 2v4M4 7l3 3M24 7l-3 3" stroke="var(--brand-blue)" stroke-width="2" fill="none"/>
        </svg>
      </span>
      <span class="service-label">Security Alarm</span>
    </li>
    <li class="service">
      <span class="service-icon">
        <svg viewBox="0 0 28 28" aria-hidden="true">
          <circle cx="15" cy="15" r="10" fill="var(--brand-blue)"/>
          <circle cx="15" cy="15" r="3" fill="var(--paper-white)"/>
          <path d="M2 10h4M2 15h4M2 20h4" stroke="var(--brand-blue)" stroke-width="2"/>
        </svg>
      </span>
      <span class="service-label">Fire Alarm</span>
    </li>
    <li class="service">
      <span class="service-icon">
        <svg viewBox="0 0 28 28" aria-hidden="true">
          <rect x="3" y="7" width="22" height="4" fill="var(--brand-blue)"/>
          <path d="M5 12h18a9 9 0 0 1-18 0z" fill="var(--brand-blue)"/>
          <circle cx="14" cy="16" r="2.5" fill="var(--paper-white)"/>
        </svg>
      </span>
      <span class="service-label">Video Surveillance</span>
    </li>
  </ul>
</section>

<section class="card card--front" aria-label="Business card front">
  <svg class="front-art" viewBox="0 0 560 320" aria-hidden="true">
    <circle cx="440" cy="120" r="200" fill="var(--paper-white)"/>
    <path d="M300 -10 A200 200 0 0 0 430 316" fill="none" stroke="var(--brand-blue)" stroke-width="3"/>
  </svg>

  <div class="brand">Vantorra<span class="brand-tagline">Security Systems</span></div>

  <div class="contact">
    <p class="person-name">MARCUS HALE</p>
    <p class="person-role">Managing Director</p>
    <ul class="contact-lines">
      <li>
        <svg viewBox="0 0 16 16" fill="var(--paper-white)" aria-hidden="true"><path d="M3 1l3 1 1 3-2 2a9 9 0 0 0 4 4l2-2 3 1 1 3-2 2C7 15 1 9 1 3z"/></svg>
        555.014.2290 ext 112
      </li>
      <li>
        <svg viewBox="0 0 16 16" aria-hidden="true"><rect x="1" y="3" width="14" height="10" fill="var(--paper-white)"/><path d="M1 3l7 6 7-6" fill="none" stroke="var(--brand-blue)" stroke-width="1.5"/></svg>
        name@vantorrainfo.com
      </li>
      <li>
        <svg viewBox="0 0 16 16" fill="none" stroke="var(--paper-white)" stroke-width="1.4" aria-hidden="true"><circle cx="8" cy="8" r="6.5"/><ellipse cx="8" cy="8" rx="3" ry="6.5"/><path d="M1.5 8h13M3 4.5h10M3 11.5h10"/></svg>
        www.vantorrainfo.com
      </li>
    </ul>
    <p class="address">4820 Lakeview Rd # 310<br>Fairmont Ohio 44210</p>
  </div>
</section>

</body>
</html>
```